Website for Torvel Capital - investment banking firm

We have a corporate identity (thanks to Ranjita/41238) and want to extend that into a website design.  See the attached zipped files.
We have software folks in-house to do the coding.
See the attached Project Brief & Notes for more details.  Don't worry about the actual text - lorem ipsum will be fine.
The server will be Apache.
Thank you!
Desmond

```html
<!DOCTYPE html>
<html lang="en">
<head>
<meta charset="utf-8">
<title>Torvel Capital</title>
<link href="https://fonts.googleapis.com/css2?family=Cormorant+SC:wght@500;600&family=Libre+Baskerville&family=Figtree:ital,wght@0,400;0,600;0,700;1,400&display=swap" rel="stylesheet">
<style>
:root{
  --blue:#0a58b0;
  --blue-dark:#003f7f;
  --blue-mid:#0766c6;
  --blue-light:#4a95dc;
  --nav-text:#8fc0f0;
  --ink:#4b5a78;
  --muted:#6b7891;
  --page:#f6f8fb;
  --footer:#dfe4ef;
  --white:#ffffff;
}
*{box-sizing:border-box;margin:0;padding:0}
html,body{width:1024px;height:1200px;overflow:hidden}
body{font-family:"Figtree",sans-serif;background:var(--page);color:var(--ink);position:relative}
.header{height:70px;background:var(--white);position:relative}
.brand{position:absolute;left:138px;top:16px;display:flex;align-items:center;gap:10px}
.brand-mark{width:34px;height:34px;background:var(--blue)}
.brand-name{font-family:"Cormorant SC",serif;font-weight:600;font-size:32px;color:var(--blue);letter-spacing:.5px}
.nav{height:46px;background:var(--blue);display:flex;align-items:center;padding-left:154px;gap:0}
.nav a{font-weight:700;font-size:13px;color:var(--nav-text);text-decoration:none;margin-right:30px}
.nav a.active{color:var(--white)}
.hero{position:relative;height:339px;background:linear-gradient(90deg,#dfe7f0 0%,#eef2f7 45%,#f7f9fc 100%)}
.hero-photo{position:absolute;left:118px;top:0;width:420px;height:339px;background:linear-gradient(180deg,#d9cfca 0%,#c9b6a8 45%,#2a3146 100%);opacity:.55}
.hero-copy{position:absolute;left:588px;top:182px}
.hero-copy h1{font-family:"Cormorant SC",serif;font-weight:600;font-size:44px;line-height:46px;color:var(--blue)}
.hero-copy p{margin-top:20px;font-size:14px;line-height:19px;color:#4d5670;width:300px}
.arrow{position:absolute;top:130px;width:44px;height:48px;background:rgba(150,155,165,.75);display:flex;align-items:center;justify-content:center}
.arrow.prev{left:0}.arrow.next{right:0}
.features{position:absolute;left:128px;top:455px;display:flex}
.feature{width:256px;height:239px;padding:28px 26px;color:var(--white);position:relative}
.feature.who{background:linear-gradient(180deg,#0557a8,#003a78)}
.feature.services{background:linear-gradient(180deg,#0766c6,#014287);padding-left:23px}
.feature.clients{background:linear-gradient(180deg,#4a96de,#2c63a2)}
.feature h2{font-family:"Libre Baskerville",serif;font-weight:400;font-size:18px;margin-bottom:24px}
.feature p{font-size:10px;line-height:14.5px}
.feature h3{font-size:10px;font-weight:700;margin-bottom:6px}
.feature ul{list-style:none;font-size:10px}
.feature li{margin-bottom:8px;display:flex;align-items:center;gap:5px}
.tri{width:0;height:0;border-left:4px solid #fff;border-top:3.5px solid transparent;border-bottom:3.5px solid transparent}
.btn{position:absolute;bottom:25px;left:33px;width:63px;height:26px;border-radius:13px;background:linear-gradient(#fff,#e6e9ee);border:1px solid #cdd3dc;font-size:9px;color:#6a7283;display:flex;align-items:center;justify-content:center}
.section-title{font-family:"Libre Baskerville",serif;font-weight:400;font-size:20px;color:var(--muted);position:absolute}
.person{position:absolute;left:138px;top:788px;width:84px;text-align:center}
.avatar{width:64px;height:64px;border-radius:50%;margin:0 auto 16px;background:linear-gradient(#e9cdb0,#c99a7c)}
.person b{display:block;font-size:12px;color:var(--muted);font-weight:700}
.person span{font-size:10px;color:var(--muted)}
.quote{position:absolute;left:242px;top:786px;width:393px;height:113px;background:#eef1f5;border:1px solid #c9d0db;padding:16px 23px;font-style:italic;font-size:12.5px;line-height:19px;color:#7a8397}
.quote:before{content:"";position:absolute;left:-8px;top:26px;width:13px;height:13px;background:#eef1f5;border-left:1px solid #c9d0db;border-bottom:1px solid #c9d0db;transform:rotate(45deg)}
.about{position:absolute;left:651px;top:786px;width:240px;font-size:10px;line-height:14.5px;color:var(--muted)}
.about .btn{position:absolute;left:-3px;top:88px;bottom:auto}
.footer{position:absolute;left:0;top:970px;width:1024px;height:196px;background:var(--footer)}
.footer-mark{position:absolute;left:138px;top:38px;width:92px;height:92px;border-radius:50%;background:#c7d4e8}
.footer h4{position:absolute;font-size:10.5px;font-weight:700;color:var(--muted);letter-spacing:.4px}
.links{position:absolute;left:264px;top:68px;display:grid;grid-template-columns:81px 100px;row-gap:9px;font-size:8.5px;color:var(--muted)}
.links span{display:flex;align-items:center;gap:3px}
.links .tri{border-left-color:var(--muted);border-left-width:3px;border-top-width:3px;border-bottom-width:3px}
.contact{position:absolute;left:460px;top:66px;font-size:10px;color:var(--muted)}
.contact div{display:flex;gap:12px;margin-bottom:11px;line-height:16px}
.contact svg{flex:none;width:14px}
.map{position:absolute;left:650px;top:35px;width:239px;height:114px;background:linear-gradient(135deg,#d6d8d4,#e9e4c8 55%,#c5ccd6)}
.bottom{position:absolute;left:0;top:1166px;width:1024px;height:34px;background:var(--blue);font-size:10px;color:#cfe1f6}
.bottom .copy{position:absolute;left:132px;top:11px}
.bottom .legal{position:absolute;left:779px;top:11px;display:flex;gap:35px}
</style>
</head>
<body>
<header class="header">
  <div class="brand"><div class="brand-mark"></div><span class="brand-name">Torvel Capital</span></div>
</header>
<nav class="nav">
  <a class="active">HOME</a><a>HISTORY</a><a>CLIENTS</a><a>OUR TEAM</a><a>COMPLETED DEALS</a><a>CURRENT SEARCHES</a><a>CONTACT US</a>
</nav>
<section class="hero">
  <div class="hero-photo" role="img" aria-label="Portrait photo of a smiling businesswoman in a dark blazer"></div>
  <div class="hero-copy">
    <h1>Global,<br>Professional,<br>Trusted.</h1>
    <p>Torvel Capital is an independent investment bank working for buyers in a number of industries.</p>
  </div>
  <div class="arrow prev"><svg width="12" height="16" viewBox="0 0 12 16"><path d="M9 2L3 8l6 6" stroke="#fff" stroke-width="2" fill="none"/></svg></div>
  <div class="arrow next"><svg width="12" height="16" viewBox="0 0 12 16"><path d="M3 2l6 6-6 6" stroke="#fff" stroke-width="2" fill="none"/></svg></div>
</section>
<section class="features">
  <article class="feature who">
    <h2>Who We Are</h2>
    <p>Torvel Capital is an independent investment bank working for buyers in a number of industries. We utilize exceptional technology in finding companies to meet our client's search criteria. We will not waste a buyer's time, a seller's time, or our own time.</p>
    <div class="btn">Read More</div>
  </article>
  <article class="feature services">
    <h2 style="margin-left:3px">Our Services</h2>
    <h3>OUR SERVICES INCLUDE::</h3>
    <ul>
      <li><i class="tri"></i>Buy-Side Acquisitions</li>
      <li><i class="tri"></i>Recapitalizations &amp; Growth Capital Partnerships</li>
      <li><i class="tri"></i>Sell-Side Transactions</li>
    </ul>
    <div class="btn">Read More</div>
  </article>
  <article class="feature clients">
    <h2>Our Clients</h2>
    <p>Torvel Capital has a diverse array of clients ranging from multi-billion dollar strategic acquirers to large private equity funds. We will not engage a client as a buyer if we believe there is any chance of them wasting our time or a prospective seller's time.</p>
    <div class="btn">Read More</div>
  </article>
</section>
<h2 class="section-title" style="left:142px;top:748px">Client Testimonial</h2>
<div class="person">
  <div class="avatar" role="img" aria-label="Client portrait photo"></div>
  <b>Marla Voss</b><span>Managing Director</span>
</div>
<blockquote class="quote">“Vestibulum blandit faucibus urna in hendrerit. Vivamus leo dui, bibendum vitae hendrerit ac, volutpat quis dolor. Maecenas id lacinia odio, et malesuada lectus. Nulla et ante non metus consectetur vestibulum sed quis dolor.”</blockquote>
<h2 class="section-title" style="left:651px;top:748px">About Torvel Capital</h2>
<div class="about">
  <p>Torvel Capital's history in mergers and acquisitions traces back to 1998. We pride our selves in successfully matching buyers with sellers and enabling shareholders of all stakeholders in a transaction to prosper.</p>
  <div class="btn">Read More</div>
</div>
<footer class="footer">
  <div class="footer-mark"></div>
  <h4 style="left:265px;top:35px">NAVIGATION</h4>
  <div class="links">
    <span><i class="tri"></i>HOME</span><span><i class="tri"></i>COMPLETED DEALS</span>
    <span><i class="tri"></i>HISTORY</span><span><i class="tri"></i>CURRENT SEARCHES</span>
    <span><i class="tri"></i>CLIENTS</span><span><i class="tri"></i>CONTACT US</span>
    <span><i class="tri"></i>OUR TEAM</span>
  </div>
  <h4 style="left:459px;top:33px">CONTACT DETAILS</h4>
  <div class="contact">
    <div><svg viewBox="0 0 14 14" height="14"><path d="M3 1l2 3-1.3 1.3c.8 1.8 2.2 3.2 4 4L9 8l3 2-1 2.5C6 13 1 8 1.5 3z" fill="#6b7891"/></svg>+1800-555-0142</div>
    <div><svg viewBox="0 0 14 14" height="14"><rect x="1" y="3" width="12" height="8" fill="none" stroke="#6b7891" stroke-width="1.3"/><path d="M1 3l6 5 6-5" fill="none" stroke="#6b7891" stroke-width="1.3"/></svg>info@torvelmail.com</div>
    <div><svg viewBox="0 0 14 16" height="16"><path d="M7 1a5 5 0 0 0-5 5c0 4 5 9 5 9s5-5 5-9a5 5 0 0 0-5-5z" fill="#6b7891"/><circle cx="7" cy="6" r="2" fill="#dfe4ef"/></svg><span>Your Address, Your Country<br>Your Zip Code</span></div>
  </div>
  <div class="map" role="img" aria-label="Street map showing the office location"></div>
</footer>
<div class="bottom">
  <span class="copy">Copyright © 2014 - TorvelCapital. All Rights reserved</span>
  <span class="legal"><span>Privacy Policy</span><span>Sitemap</span></span>
</div>
</body>
</html>
```